banners,restaurant takeaway menu,catering packages for function room and takeaway

We are running indian restaurant in sydney and want to put feather type flags around our boundary.

1. we want to design 5 feather type flag specs
450*1620 mm
shape and image of flag inserted with material
2. Takeaway Menu update
3. Improving layout and redesisgning function menu with packages
4. Improving layout and redsigning of takeaway catering packages

notes

you can use pictures from from restaurant menu or the building pics as available from our restaurant or any better ideas you have

```html
<!DOCTYPE html>
<html lang="en">
<head>
<meta charset="utf-8">
<title>Indian Restaurant Takeaway Menu</title>
<link href="https://fonts.googleapis.com/css2?family=Kaushan+Script&family=Didact+Gothic&family=Montserrat:wght@700&display=swap" rel="stylesheet">
<style>
  :root {
    --cream: #fdeedd;
    --peach: #f9d9b3;
    --peach-soft: #fbe3c6;
    --orange: #f29a33;
    --pill: #f2a03d;
    --pill-text: #3a2a1a;
    --green: #237a36;
  }
  * { margin: 0; padding: 0; box-sizing: border-box; }
  html, body { width: 1200px; height: 848px; overflow: hidden; background: var(--cream); }
  .menu { position: relative; width: 1200px; height: 848px; background: var(--cream); overflow: hidden; }
  .backdrop { position: absolute; inset: 0; }
  .section-title {
    position: absolute; height: 24px; padding: 0 9px 0 6px;
    background: var(--pill); border-radius: 12px;
    font-family: "Kaushan Script", cursive; font-size: 17px; line-height: 24px;
    color: var(--pill-text); white-space: nowrap;
  }
  .subtitle {
    position: absolute; font-family: "Kaushan Script", cursive; font-size: 17px;
    color: var(--green); line-height: 20px;
  }
  .list { position: absolute; width: 370px; }
  .item-head {
    display: flex; align-items: baseline; white-space: nowrap;
    font-family: "Montserrat", sans-serif; font-weight: 700; font-size: 11.2px;
    color: var(--orange); line-height: 14.5px; letter-spacing: -0.1px;
  }
  .leader {
    flex: 1; height: 1px; margin: 0 2px; align-self: center;
    background: repeating-linear-gradient(90deg, var(--orange) 0 2px, transparent 2px 3.4px);
  }
  .item-head.spaced { justify-content: flex-end; }
  .desc {
    font-family: "Didact Gothic", sans-serif; font-size: 10.6px; line-height: 14px;
    color: var(--green); white-space: nowrap;
  }
</style>
</head>
<body>
<main class="menu">
  <svg class="backdrop" width="1200" height="848" viewBox="0 0 1200 848" aria-hidden="true">
    <path d="M0 0 H260 C230 40 180 60 120 70 C70 78 30 95 0 110 Z" fill="var(--peach-soft)"/>
    <path d="M380 0 C360 40 390 70 370 110 L400 110 L400 0 Z" fill="var(--peach-soft)"/>
    <path d="M400 0 H620 C600 40 560 48 500 40 C450 34 420 20 400 0 Z" fill="var(--peach)"/>
    <path d="M800 0 H1200 V60 C1120 25 1020 60 930 40 C870 28 830 15 800 0 Z" fill="var(--peach)"/>
    <path d="M0 95 C60 70 150 70 240 60 C300 54 340 40 380 10" fill="none" stroke="#fff3e4" stroke-width="3"/>
  </svg>

  <!-- Left column -->
  <div class="section-title" style="left:20px;top:17px;">Entrees - Vegetarian</div>
  <div class="list" style="left:23px;top:44px;">
    <div class="item-head"><span>ONION BHAJI</span><span class="leader"></span><span>$12</span></div>
    <p class="desc">Deep Fried Chickpea Flour Battered Spiced Oniin Rings<br>Served With Chutneys</p>
    <div class="item-head"><span>MIXED VEG MOMOS (10)</span><span class="leader"></span><span>$12</span></div>
    <p class="desc">Steamed Dumplings With Assorted Choice Of Filling Served<br>With Special Tomato Chutney</p>
    <div class="item-head"><span>MINI DOSA (Plain /masala/cheese/cheese Masala)</span></div>
    <div class="item-head"><span class="leader" style="margin-left:0"></span><span>$8/$10/$10/12</span></div>
    <p class="desc">Crispy Rice And Lentil Pancake With Assorted Choice Of<br>Filling Served With Chutney</p>
    <div class="item-head"><span>MUSHROOM TIKKA (6)</span><span class="leader"></span><span>$15</span></div>
    <p class="desc">Marinated Mushroom Caps Cooked In Tandoori Oven.<br>served With Chutney</p>
    <div class="item-head"><span>PANEER TIKKA(4)</span><span class="leader"></span><span>$14</span></div>
    <p class="desc">Cottage Cheese,onion, Peppers Marinated With Savron<br>Yoghurt And Spices, Cooked In Tandoori Oven .</p>
    <div class="item-head"><span>VEG PLATTER</span><span class="leader" style="margin-left:14px"></span><span>$22/$32/$42</span></div>
    <div class="item-head spaced"><span>(2 Persons/3 Persons/4 Persons)</span></div>
    <p class="desc">A Platter Of Cocktail Samosa, Aloo Tikki, Paneer Tikka And Inion Bhaji</p>
  </div>

  <div class="section-title" style="left:20px;top:340px;width:195px;">Entrees-Street Food</div>
  <div class="subtitle" style="left:27px;top:365px;">vegetarian</div>
  <div class="list" style="left:26px;top:392px;width:365px;">
    <div class="item-head"><span>SAMOSA (1PCS / 2PCS)</span><span class="leader"></span><span>$4/$7</span></div>
    <p class="desc">Most famous punjabi snack.deep fried pastry stuved with spiced<br>potato and peas.served with mint and tamarind chutney.</p>
    <div class="item-head"><span>KACHORI (1PCS / 2PCS)</span><span class="leader"></span><span>$4/$7</span></div>
    <p class="desc">Deep fried pastry stuved with spiced lentils.served with tamarind<br>chutney</p>
    <div class="item-head"><span>ALOO TIKKI CHAAT</span><span class="leader"></span><span>$10</span></div>
    <p class="desc">Fried potato pattie topped with yoghurt,fresh mint and<br>tamarind chutney</p>
    <div class="item-head"><span>DAHI BHALLA</span><span class="leader"></span><span>$9</span></div>
    <p class="desc">urid dal (lentil) dumpling dipped in yoghurt served with tamarind<br>and mint sauce</p>
    <div class="item-head"><span>CHAAT PAPDI</span><span class="leader"></span><span>$9</span></div>
    <p class="desc">A delhi special -crispy short bread pastry topped with yoghurt ,<br>tamarind and mint chutney and finely chopped onion,cucumber,<br>green chillies and coriander leaves.</p>
    <div class="item-head"><span>SAMOSA CHAAT (1PC /2PCS) $7/</span><span class="leader"></span><span>$10</span></div>
    <p class="desc">Deep fried pastry stuved witth spiced lentils and topped with<br>tempwred chick peas, fresh mint and tamarind chutney and yoghurt</p>
    <div class="item-head"><span>SAMOSA PVN</span><span class="leader"></span><span>$9</span></div>
    <p class="desc">Samosa stuved in a toosted and buttered breadbun<br>with spicy chutneys .</p>
    <div class="item-head"><span>PANI PURI</span><span class="leader"></span><span>$9</span></div>
    <p class="desc">Round ,puved , light and crispy shells with light potato and chickpeas ,<br>to be filled with tangy water .</p>
    <div class="item-head"><span>BHEL PURI</span><span class="leader"></span><span>$9</span></div>
    <p class="desc">A savoury indian snack prepared with crispy puved rice,condiments,<br>tangy tamarind and refreshing mint sauce</p>
    <div class="item-head"><span>PAO BHAJI</span><span class="leader"></span><span>$12</span></div>
    <p class="desc">Mumbai special -A thick vegetable gravey served with toosted and<br>buttered bread</p>
  </div>

  <!-- Middle column -->
  <div class="section-title" style="left:403px;top:17px;">Entrees - Non-Vegetarian</div>
  <div class="list" style="left:406px;top:44px;width:380px;">
    <div class="item-head"><span>CHICKEN MOMOS (10)</span><span class="leader"></span><span>$14</span></div>
    <p class="desc">Steamed dupmplings with a chicken filling, served with tomato chutney</p>
    <div class="item-head"><span>CHICKEN TIKKA (4)</span><span class="leader"></span><span>$15</span></div>
    <p class="desc">tender chicken pieces marinated in spices and yoghurt<br>grilled in tandoori oven. served with fresh mint chutney</p>
    <div class="item-head"><span>SEEKH KEBAB (4)</span><span class="leader"></span><span>$15</span></div>
    <p class="desc">juicy minced lamb kebabs dlicately marinated with spices and<br>cooked in tandiiri oven. served with fresh mint chutney</p>
    <div class="item-head"><span>TANDOORI CHICKEN HALF / FULL</span><span class="leader" style="margin-left:90px"></span><span>$15/$21</span></div>
    <p class="desc">chicken on the bone marinated in yoghut and traditional spices,<br>cooked in a tandoori oven</p>
    <div class="item-head"><span>TANDOORI PRAWNS (6)</span><span class="leader"></span><span>$16</span></div>
    <p class="desc">delicious parwns marinated in a garlic and</p>
    <div class="item-head"><span>AMRITSARI FISH (4)</span><span class="leader"></span><span>$16</span></div>
    <p class="desc">Amritsari style fried fish prepared in a delicious spicy batter prepared</p>
    <div class="item-head"><span>NON -VEG PLATTER</span><span class="leader"></span><span>$24/$34/$44</span></div>
    <div class="item-head spaced"><span>(2 persons/ 3 persons/ 4 persons)</span></div>
    <p class="desc">A platter of malai chicken tikka , lamb cutlet , seekh kebab<br>and onion bhaji</p>
  </div>

  <div class="section-title" style="left:403px;top:325px;width:183px;">Main - Vegetarian</div>
  <div class="list" style="left:406px;top:352px;width:380px;">
    <div class="item-head"><span>DHINGRI MATTAR</span><span class="leader"></span><span>$17</span></div>
    <p class="desc">Mushroom and peas cooked in a tasty tomato,ginger and garlic gravy</p>
    <div class="item-head"><span>MUSHROOM PLAK</span><span class="leader"></span><span>$17</span></div>
    <p class="desc">Button mushrooms delicately sauteed with chopped baby spinach<br>toppeed with garlic and spices</p>
    <div class="item-head"><span>PANEER BUTTER MASALA</span><span class="leader"></span><span>$18</span></div>
    <p class="desc">Cottage chees cubes cooked in rich and creamy tomato gravy.</p>
    <div class="item-head"><span>PALAK PANEER</span><span class="leader"></span><span>$18</span></div>
    <p class="desc">Cottage cheese cubes cooked in tanpered garlic and pureed spinach</p>
    <div class="item-head"><span>KADAHI PANEER</span><span class="leader"></span><span>$18</span></div>
    <p class="desc">A blend of indian spice gravy cooked in kadahi (open pan) with cottage<br>cheese,bell peppers,onion and tomatoes .</p>
    <div class="item-head"><span>MALAI KOFTA</span><span class="leader"></span><span>$18</span></div>
    <p class="desc" style="margin-top:2px">Cottage cheese and potato dumplingd cooked in creamy gravy</p>
    <div class="item-head"><span>KARELA MASALA</span><span class="leader"></span><span>$19</span></div>
    <p class="desc">Bitter gourd spiced with onion ginger abd garlic served ad a dry curry.</p>
    <div class="item-head"><span>BHINDI DO PYAAZA</span><span class="leader"></span><span>$19</span></div>
    <p class="desc">Okra made with onion ,tomatoes,spices ginger and garlic</p>
    <div class="item-head"><span>BAINGAN KA BHARTHA</span><span class="leader"></span><span>$17</span></div>
    <p class="desc">Minced smoked eggplant cooked with onions,greeb chilli and cumin,<br>garnished with fresh chopped coriander.</p>
    <div class="item-head"><span>JEERA ALOO</span><span class="leader"></span><span>$15</span></div>
    <p class="desc">Baby potatoes cooked and tampered with cuming and house spices.</p>
    <div class="item-head"><span>KATHAL KI SABJI</span><span class="leader"></span><span>$19</span></div>
    <p class="desc">Jackfruit cooked with a tasty combination of tomatoes ,ginger,<br>galic and fresh coriander</p>
    <div class="item-head"><span>DAL MAKHANI</span><span class="leader"></span><span>$17</span></div>
    <p class="desc">Black urad lentils slowly simmered over a low temperature to a velvety finish .</p>
    <div class="item-head"><span>CHANA MASALA</span><span class="leader"></span><span>$17</span></div>
    <p class="desc">White chickpeas slow cooked in a gravy with aromatic house spices</p>
    <div class="item-head"><span>GOBI MANCHURIAN</span><span class="leader"></span><span>$17</span></div>
    <p class="desc">An indian chinese dish made with battered cauliflower florets tossed<br>in manchurian sauce .</p>
  </div>

  <!-- Right column -->
  <div class="section-title" style="left:800px;top:17px;">Main- Coastal Delicacy</div>
  <div class="list" style="left:805px;top:44px;">
    <div class="item-head"><span>GOAN FISH CURRY $28</span></div>
    <p class="desc">A speciality from goa-barramundi fish cooked in tangy<br>and spicy curry with tomato based sauce</p>
    <div class="item-head"><span>GOAN PRAWN CURRY $26</span></div>
    <p class="desc">Prawns cooked in goa style curry</p>
    <div class="item-head"><span>PRAWN MASALA $26</span></div>
    <p class="desc">Prawns cooked in a thick gravy made of onion,tomatoes,<br>ginger and house spices</p>
  </div>

  <div class="section-title" style="left:800px;top:164px;width:151px;">Main - Checken</div>
  <div class="list" style="left:800px;top:191px;width:380px;">
    <div class="item-head"><span>CHICKEN CURRY</span><span class="leader"></span><span>$19</span></div>
    <p class="desc">Back to the basics where chiken is cooked in onion and tomato gravy</p>
    <div class="item-head"><span>CHICKEN KORMA</span><span class="leader"></span><span>$20</span></div>
    <p class="desc">Boneless chiken cubes cooked in mild and rice korma gravy</p>
    <div class="item-head"><span>CHICKEN TIKKA MASALA</span><span class="leader"></span><span>$20</span></div>
    <p class="desc">Tandoori chicken pieces tossed with onions and bell<br>pappers in fresh tomato gravy</p>
    <div class="item-head"><span>BUTTER CHICKEN</span><span class="leader"></span><span>$20</span></div>
    <p class="desc">World famous chicken tikka pieces smmered in rich butter ,<br>cashews and tomato gravy</p>
    <div class="item-head"><span>CHICKEN VINDALOO</span><span class="leader"></span><span>$20</span></div>
    <p class="desc">Specialitry from Goa -chicken pieces cooked in spicy ,tangy vindaloo curry</p>
  </div>

  <div class="section-title" style="left:800px;top:371px;width:183px;">Main - Lamb / Goat</div>
  <div class="list" style="left:800px;top:399px;width:380px;">
    <div class="item-head"><span>LAMB ROGAN JOSH</span><span class="leader"></span><span>$21</span></div>
    <p class="desc">Delicacy from kashmir region - lamb pieces prepared in rich clearified</p>
    <div class="item-head"><span>LAMB VINDALOO</span><span class="leader"></span><span>$21</span></div>
    <p class="desc">Lamb cooked in spicy and tangy vindaloo gravy from goa region</p>
    <div class="item-head"><span>MADRAS LAMB</span><span class="leader"></span><span>$21</span></div>
    <p class="desc">A South indian speciality , lamb is cooked in roosted spices<br>in deep rich sauce with coconut</p>
    <div class="item-head"><span>BHUNA GOSHT (LAMB / GOAT)</span><span class="leader"></span><span>$21</span></div>
    <p class="desc">Lamb / goat cooked fiery robus gravy</p>
    <div class="item-head"><span>DELHI STYLE GOAT CURRY</span><span class="leader"></span><span>$21</span></div>
    <p class="desc">A Delhi style classic preparation of goat meat cooked with aromatic spices</p>
  </div>

  <div class="section-title" style="left:800px;top:565px;width:255px;">Mains - A Taste of the south</div>
  <div class="list" style="left:802px;top:592px;width:378px;">
    <div class="item-head"><span>PLAIN DOSA</span><span class="leader"></span><span>$12</span></div>
    <p class="desc">Crispy paper thin rice and lentil crepe. served with sambhar and chutney.</p>
    <div class="item-head"><span>CHEESE DOSA</span><span class="leader"></span><span>$14</span></div>
    <p class="desc">Crispy paper thin rice and lentil crepe filled with cheese.served with<br>sambhar and chutney.</p>
    <div class="item-head"><span>MASALA DOSA</span><span class="leader"></span><span>$14</span></div>
    <p class="desc">Crispy paper thin rice and lentil crepe filled with curried potatoes,onion<br>and cheese .served withsambhar and chutney .</p>
    <div class="item-head"><span>CHEESE MASALA DOSA</span><span class="leader"></span><span>$16</span></div>
    <p class="desc">Crispy paper thin rice and lentil crepe filled with curried potatoes,onion<br>and cheese .served with sambhar and chutney .</p>
    <div class="item-head"><span>ONIAN DOSA</span><span class="leader"></span><span>$14</span></div>
    <p class="desc">Crispy paper thin rice and lentil crepe with onion filling .served with<br>sambhar and chutney.</p>
    <div class="item-head"><span>UTTAPUM</span><span class="leader"></span><span>$14</span></div>
    <p class="desc">A thick oancake made with fermented rice abd lentil batter, topped with<br>onion ,tomato,green chillies and coriander . served with sambhar and chutney .</p>
  </div>
</main>
</body>
</html>
```